Billboard for Window Tinting, Paint Protection & CAR Wrapping.

I need design for Billboard which will come on the side on my Garage. I have Window tinting shop and i want that on this Billboard there are Pictures and Text what i am doing. So measures from Billboard: 12,6 meter long and high 1,76Meter high.
I will upload one billboard which i already have it on the street where cars drives on the side, so that yo can see the style how i want it.
This new one schuld have my logo on the blackbackground and 3 Pictures what i am doing(SCHEIBENTÖNUNG/ WINDOW TINTING, LACKSCHUTZFOLIERUNG(PAINT PROTECTION, AUTOFOLIERUNG/CAR WRAPPING) So for each kategory it has to be one picture. I will upolad some pictures form pixelkorb but i dont know in which format do you need.
Pleas let me k now wchich size i have to buy it on pixelkorb so that will be perfect picture.
Aso my website: www.veltramo-scheibentoenung.at
On the billboard schould also stay infos:
web: www.veltramo-scheibentoenung.at
Ikon for Chatterly: Veltramo-scheibentönung
Tel: 070319827
Tel: 06642915073

Target Market(s)

People with cars. I am making window tint on the cars an also paint Protection and Car Wrapping

Industry/Entity Type

Automotive

Colors
000000
9a9a9a

Requirements
Must have
• very good pictures
Nice to have
• The Goal from this Billboard is, when customers comes with the car to my garage, that they see a Huge Billboard and in 2 seconds he recognise what i am doing(Window tint, PaintProtection ,Car Wrapping) It will be written but the Photos has to be HOT realy Amazing with combination with my Logo.

```html
<!DOCTYPE html>
<html lang="de">
<head>
<meta charset="utf-8">
<title>Veltramo Billboard</title>
<link rel="stylesheet" href="https://fonts.googleapis.com/css2?family=Oswald:wght@400;500;700&display=swap">
<style>
  :root {
    --stage: #a7a8aa;
    --black: #0d0d0d;
    --silver: #9a9a9a;
    --red: #d11a22;
    --red-dark: #8e0e14;
    --white: #ffffff;
  }
  html, body {
    margin: 0;
    width: 1200px;
    height: 414px;
    overflow: hidden;
    background: var(--stage);
  }
  .billboard {
    position: absolute;
    left: 34px;
    top: 54px;
    width: 1130px;
    height: 282px;
    box-shadow: 0 10px 14px rgba(0,0,0,0.35);
  }
  .billboard svg { display: block; }
  .brand-name, .band-label, .phone-text, .web-address {
    font-family: "Oswald", sans-serif;
  }
  .brand-name { font-weight: 700; font-size: 48px; fill: var(--red); }
  .web-address { font-weight: 500; font-size: 14px; fill: var(--white); }
  .phone-text { font-weight: 500; font-size: 19px; fill: var(--white); }
  .band-label { font-weight: 500; font-size: 19px; fill: var(--white); }
</style>
</head>
<body>
<div class="billboard">
  <svg width="1130" height="282" viewBox="0 0 1130 282" xmlns="http://www.w3.org/2000/svg">
    <defs>
      <radialGradient id="panel-black" cx="0.45" cy="0.3" r="0.85">
        <stop offset="0" stop-color="#3d3d3f"/>
        <stop offset="1" stop-color="#080808"/>
      </radialGradient>
      <linearGradient id="tone-tint" x1="0" y1="0" x2="1" y2="0.6">
        <stop offset="0" stop-color="#bfbfc1"/>
        <stop offset="0.2" stop-color="#2a2a2c"/>
        <stop offset="0.45" stop-color="#5a5a5c"/>
        <stop offset="0.7" stop-color="#1a1a1b"/>
        <stop offset="1" stop-color="#7d7d80"/>
      </linearGradient>
      <linearGradient id="tone-paint" x1="0" y1="0" x2="0.8" y2="1">
        <stop offset="0" stop-color="#a9abae"/>
        <stop offset="0.35" stop-color="#6e7073"/>
        <stop offset="0.65" stop-color="#2e2f31"/>
        <stop offset="0.9" stop-color="#8a2a30"/>
        <stop offset="1" stop-color="#b8b8ba"/>
      </linearGradient>
      <linearGradient id="tone-wrap" x1="0" y1="0" x2="0.6" y2="1">
        <stop offset="0" stop-color="#e4e6e8"/>
        <stop offset="0.3" stop-color="#5f7585"/>
        <stop offset="0.55" stop-color="#1f2d36"/>
        <stop offset="0.8" stop-color="#3f5260"/>
        <stop offset="1" stop-color="#c9cdd0"/>
      </linearGradient>
      <linearGradient id="band-red" x1="0" y1="0" x2="0" y2="1">
        <stop offset="0" stop-color="#e0232b"/>
        <stop offset="1" stop-color="#8e0e14"/>
      </linearGradient>
      <linearGradient id="chrome" x1="0" y1="0" x2="0" y2="1">
        <stop offset="0" stop-color="#f0f0f0"/>
        <stop offset="0.5" stop-color="#8c8c8c"/>
        <stop offset="1" stop-color="#e4e4e4"/>
      </linearGradient>
    </defs>

    <g class="photo" role="img" aria-label="Foto: Scheibentönung, Hände bringen Tönungsfolie an einer Autoscheibe an">
      <polygon points="284,0 578,0 692,154 580,282 284,282 400,142" fill="url(#tone-tint)"/>
    </g>
    <g class="photo" role="img" aria-label="Foto: Lackschutzfolierung, transparente Folie wird auf eine Motorhaube gerakelt">
      <polygon points="574,0 858,0 970,148 860,282 580,282 692,154" fill="url(#tone-paint)"/>
    </g>
    <g class="photo" role="img" aria-label="Foto: Autofolierung, Fahrzeug wird in der Werkstatt mit Folie beklebt">
      <polygon points="854,0 1130,0 1130,282 860,282 970,148" fill="url(#tone-wrap)"/>
    </g>

    <polygon class="brand-panel" points="0,0 284,0 400,142 284,282 0,282" fill="url(#panel-black)"/>

    <g class="chevron-lines" fill="none">
      <polyline points="290,-4 408,142 290,286" stroke="url(#chrome)" stroke-width="9"/>
      <polyline points="570,-4 686,154 572,286" stroke="url(#chrome)" stroke-width="7"/>
      <polyline points="582,-4 698,154 584,286" stroke="var(--red)" stroke-width="4"/>
      <polyline points="850,-4 964,148 852,286" stroke="url(#chrome)" stroke-width="7"/>
      <polyline points="862,-4 976,148 864,286" stroke="var(--red)" stroke-width="4"/>
    </g>

    <circle class="brand-mark" cx="156" cy="75" r="33" fill="none" stroke="var(--red)" stroke-width="5"/>
    <text class="brand-name" x="30" y="164" textLength="254" lengthAdjust="spacing">VELTRAMO</text>
    <text class="web-address" x="51" y="209" textLength="192" lengthAdjust="spacingAndGlyphs">www.veltramo-scheibentoenung.at</text>

    <rect class="service-band" x="310" y="235" width="820" height="29" fill="url(#band-red)"/>

    <path class="phone-pill" d="M0,232 H276 a10,10 0 0 1 10,10 V256 a10,10 0 0 1 -10,10 H0 Z" fill="url(#band-red)"/>
    <g class="phone-icon" transform="translate(33,249)">
      <circle r="8" fill="none" stroke="var(--white)" stroke-width="1.6"/>
      <path d="M-3.5,-4 q-1,3 1.5,6 q2.5,2.8 5.5,2 l0.6,-1.8 -2.2,-1.2 -1,1 q-1.6,-0.6 -2.6,-2.6 l1,-1 -1.2,-2.2 z" fill="var(--white)"/>
    </g>
    <text class="phone-text" x="54" y="256" textLength="217" lengthAdjust="spacing">070319827  |  06642915073</text>

    <g class="band-labels">
      <text class="band-label" x="364" y="257">»</text>
      <text class="band-label" x="388" y="257" textLength="136" lengthAdjust="spacing">SCHEIBENTÖNUNG</text>
      <text class="band-label" x="642" y="257">»</text>
      <text class="band-label" x="664" y="257" textLength="180" lengthAdjust="spacing">LACKSCHUTZFOLIERUNG</text>
      <text class="band-label" x="944" y="257">»</text>
      <text class="band-label" x="968" y="257" textLength="121" lengthAdjust="spacing">AUTOFOLIERUNG</text>
    </g>
  </svg>
</div>
</body>
</html>
```